Enterprise Application UI beautification

We have an enterprise application that is being redesigned. A screenshot from the new UX/UI is provided. The current UI design is OK but we would like it to look better. The key goals of the UI are to look like a premium product (think luxury brand) and for it to be visually very appealing/attractive. When people see the UI we want them to have a significant, positive reaction. They should "ooh" and "ahh". This is a product sold to large enterprises, not consumers. The current UI is a little plain. The colors we want to use are blue, yellow, black, white and gray. We probably don't want different colors but feel free to use any variations within or close to that color scheme that you see fit. Also feel free to modify the spacing, icons, widgets, tables, fonts, etc.

Target Market(s)

Large enterprise customers (Summit 300).

Number of Pages Required

1 page

Font styles to use
Sans Serif

Colors
3277b5

Requirements
Must have
• A premium feel.

```html
<!DOCTYPE html>
<html lang="en">
<head>
<meta charset="utf-8">
<title>Data Sources – Cloudforge Sandbox</title>
<link href="https://fonts.googleapis.com/css2?family=Poppins:wght@300;400;500&display=swap" rel="stylesheet">
<style>
:root{
  --blue:#3277b5;
  --blue-dark:#05477c;
  --blue-mid:#1f64a0;
  --ink:#1f2a3a;
  --muted:#6b7686;
  --line:#e3e6ec;
  --panel:#f4f6fa;
  --white:#ffffff;
  --row-alt:#f6f7fa;
  --head:#eef0f4;
  --check:#3d86c8;
  --icon:#c9ced6;
  --violet:#9b4dd6;
  --green:#2bb673;
}
*{box-sizing:border-box;margin:0;padding:0}
html,body{width:1200px;height:1000px;overflow:hidden;background:var(--white);font-family:"Poppins",sans-serif;color:var(--ink)}
.app{position:absolute;left:0;top:144px;width:1200px;height:711px;background:linear-gradient(180deg,var(--blue) 0%,var(--blue-dark) 100%);overflow:hidden}
.topbar-user{position:absolute;right:14px;top:7px;color:var(--white);font-size:10px;display:flex;align-items:center;gap:4px}
.brand{position:absolute;left:18px;top:30px;display:flex;align-items:center;gap:6px;color:var(--white);font-size:13px;font-weight:500}
.brand-dot{width:10px;height:10px;border-radius:50%;background:var(--white)}
.nav-icon{position:absolute;left:35px;width:24px;height:24px;color:var(--white)}
.nav-active{position:absolute;left:17px;top:280px;width:90px;height:62px;background:var(--white);border-radius:31px 0 0 31px}
.nav-active .nav-icon{left:18px;top:19px;color:var(--blue-mid)}
.list-panel{position:absolute;left:96px;top:27px;width:285px;height:684px;background:var(--white);border-radius:14px 0 0 0}
.main{position:absolute;left:381px;top:27px;width:819px;height:684px;background:var(--panel)}
.h-title{font-weight:300;color:var(--ink)}
.pill{display:inline-flex;align-items:center;gap:3px;height:18px;padding:0 7px;border-radius:9px;background:var(--blue);color:var(--white);font-size:9.5px;box-shadow:0 3px 6px rgba(50,119,181,.3)}
.pill svg{width:8px;height:8px}
.sources-head{position:absolute;left:37px;top:38px;display:flex;align-items:center;gap:8px}
.sources-head .h-title{font-size:16px}
.search{position:absolute;left:23px;top:68px;width:221px;height:27px;border:1px solid var(--line);border-radius:14px;font-size:10px;display:flex;align-items:center;justify-content:space-between;padding:0 10px 0 18px}
.search svg{width:14px;height:14px;color:var(--muted)}
.source{position:absolute;left:13px;width:245px;height:67px;border-bottom:1px solid var(--line);padding:20px 0 0 28px}
.source.is-active{background:#efefef;border-bottom:none}
.source-name{font-size:13px;font-weight:400;line-height:1.2}
.source-type{font-size:9px;color:var(--muted)}
.list-scroll{position:absolute;left:270px;top:122px;width:5px;height:544px;border-radius:3px;background:#f1f2f4}
.list-scroll::after{content:"";position:absolute;left:0;top:0;width:5px;height:240px;border-radius:3px;background:#e6e8eb}
.detail-head{position:absolute;left:29px;top:31px;display:flex;align-items:center}
.detail-head .h-title{font-size:25px;margin-right:17px}
.detail-head .pill{margin-right:23px}
.test-conn{position:absolute;right:33px;top:40px}
.info-card{position:absolute;left:29px;top:73px;width:757px;height:109px;background:var(--white);border-radius:6px;box-shadow:0 6px 18px rgba(20,40,80,.05)}
.info-col{position:absolute;top:10px;width:330px}
.info-col.right{left:375px;border:none}
.info-col.left{left:15px}
.info-divider{position:absolute;left:329px;top:10px;width:1px;height:88px;background:var(--line)}
.info-row{display:flex;align-items:baseline;font-size:11px;height:19px}
.info-label{width:143px;display:flex;align-items:baseline;white-space:nowrap}
.info-label::after{content:"";flex:1;border-bottom:1px dotted var(--line);margin:0 4px}
.info-value{color:var(--blue)}
.objects-head{position:absolute;left:43px;top:201px;display:flex;align-items:center;gap:7px}
.objects-head .h-title{font-size:17px}
.object-tabs{position:absolute;left:43px;top:233px;display:flex;align-items:center;font-size:12px;gap:5px}
.object-tabs .fields{margin-left:28px;display:flex;align-items:center;gap:7px}
.x{color:var(--blue);width:9px;height:9px}
.table-card{position:absolute;left:27px;top:237px;width:763px;height:395px;background:var(--white);border-radius:6px;box-shadow:0 6px 18px rgba(20,40,80,.05)}
.table-card{top:264px}
.grid{position:absolute;left:16px;top:14px;width:716px}
.grid-row{position:relative;height:33px;font-size:10px;color:var(--muted)}
.grid-row.head{height:33px;background:var(--head);color:var(--ink);font-size:10px}
.grid-row.alt{background:var(--row-alt)}
.cell{position:absolute;top:0;height:33px;display:flex;align-items:center}
.c-name{left:14px}.c-type{left:200px}.c-pk{left:348px}.c-rule{left:431px;gap:4px}.c-sens{left:538px;gap:6px}.c-act{left:650px;gap:7px}
.grid-row.head .c-pk{left:342px}.grid-row.head .c-rule{left:444px}.grid-row.head .c-sens{left:542px}.grid-row.head .c-act{left:654px}
.radio{width:11px;height:11px;border:1px solid var(--check);border-radius:50%;margin-left:6px}
.radio.on{background:var(--check);display:flex;align-items:center;justify-content:center}
.radio.on svg{width:7px;height:7px;color:var(--white)}
.ri{width:9px;height:9px;color:var(--icon)}
.ri.dark{color:#5a6270}
.rl{font-size:13px;line-height:1;color:var(--icon)}
.rl.dark{color:#4b5361}.rl.violet{color:var(--violet)}
.ri.green{color:var(--green)}
.act{width:11px;height:11px;color:var(--blue-mid)}
.group{position:relative;height:41px;border-bottom:1px solid var(--line);display:flex;align-items:center;gap:5px;padding-left:14px;font-size:10px;color:var(--ink)}
.group:first-of-type{height:38px}
.chev{width:9px;height:9px;color:var(--blue)}
.table-scroll{position:absolute;right:16px;top:12px;width:6px;height:370px;border-radius:3px;background:#f2f3f5}
.table-scroll::after{content:"";position:absolute;left:0;top:0;width:6px;height:236px;border-radius:3px;background:#e6e8eb}
</style>
</head>
<body>
<svg width="0" height="0" style="position:absolute">
  <defs>
    <symbol id="i-cal" viewBox="0 0 24 24"><g fill="none" stroke="currentColor" stroke-width="1.8"><rect x="3" y="5" width="18" height="16" rx="2"/><path d="M3 10h18M8 3v4M16 3v4"/><path d="M7 13h2M11 13h2M15 13h2M7 17h2M11 17h2M15 17h2"/></g></symbol>
    <symbol id="i-db" viewBox="0 0 24 24"><g fill="none" stroke="currentColor" stroke-width="1.8"><ellipse cx="9" cy="5" rx="6" ry="2.5"/><path d="M3 5v12c0 1.4 2.7 2.5 6 2.5M3 9c0 1.4 2.7 2.5 6 2.5M3 13c0 1.4 2.7 2.5 6 2.5"/><ellipse cx="15.5" cy="11" rx="5.5" ry="2.3"/><path d="M10 11v9c0 1.3 2.5 2.3 5.5 2.3s5.5-1 5.5-2.3v-9M10 14c0 1.3 2.5 2.3 5.5 2.3S21 15.3 21 14M10 17c0 1.3 2.5 2.3 5.5 2.3S21 18.3 21 17"/></g></symbol>
    <symbol id="i-bank" viewBox="0 0 24 24"><g fill="none" stroke="currentColor" stroke-width="1.8"><path d="M2 9l10-6 10 6z"/><path d="M3 21h18M4 18h16M6 10v8M10 10v8M14 10v8M18 10v8"/></g></symbol>
    <symbol id="i-docs" viewBox="0 0 24 24"><g fill="none" stroke="currentColor" stroke-width="1.8"><rect x="8" y="2" width="12" height="15" rx="1.5"/><path d="M5 6v14a1.5 1.5 0 0 0 1.5 1.5H16"/><path d="M11 7h6M11 11h6"/></g></symbol>
    <symbol id="i-x" viewBox="0 0 10 10"><path d="M1.5 1.5l7 7M8.5 1.5l-7 7" stroke="currentColor" stroke-width="1.6" fill="none"/></symbol>
    <symbol id="i-pen" viewBox="0 0 12 12"><g fill="none" stroke="currentColor" stroke-width="1.1"><path d="M2 10l.6-2.6L8.4 1.6l2 2-5.8 5.8z"/><path d="M7.4 2.6l2 2"/></g></symbol>
    <symbol id="i-search" viewBox="0 0 16 16"><g fill="none" stroke="currentColor" stroke-width="1.8"><circle cx="7" cy="7" r="5"/><path d="M11 11l4 4"/></g></symbol>
    <symbol id="i-copy" viewBox="0 0 10 10"><g fill="none" stroke="currentColor" stroke-width="1.4"><rect x="3.5" y="1" width="5.5" height="5.5"/><path d="M1 3.5V9h5.5"/></g></symbol>
    <symbol id="i-fork" viewBox="0 0 10 10"><g fill="none" stroke="currentColor" stroke-width="1.2"><circle cx="2" cy="2" r="1.2"/><circle cx="8" cy="2" r="1.2"/><path d="M2 3.2v1.5c0 1 3 1 3 2.5V9M8 3.2v1.5c0 1-3 1-3 2.5"/></g></symbol>
    <symbol id="i-ring" viewBox="0 0 10 10"><circle cx="5" cy="5" r="3.2" fill="none" stroke="currentColor" stroke-width="1.3"/></symbol>
    <symbol id="i-play" viewBox="0 0 10 10"><path d="M3 2l4.5 3L3 8z" fill="currentColor"/></symbol>
    <symbol id="i-tick" viewBox="0 0 10 10"><path d="M2 5.2l2 2 4-4.4" fill="none" stroke="currentColor" stroke-width="1.8"/></symbol>
    <symbol id="i-chev-down" viewBox="0 0 10 10"><path d="M1.5 3.5L5 7l3.5-3.5" fill="none" stroke="currentColor" stroke-width="1.5"/></symbol>
    <symbol id="i-chev-up" viewBox="0 0 10 10"><path d="M1.5 6.5L5 3l3.5 3.5" fill="none" stroke="currentColor" stroke-width="1.5"/></symbol>
    <symbol id="i-clip" viewBox="0 0 10 10"><g fill="none" stroke="currentColor" stroke-width="1"><rect x="1.5" y="1" width="7" height="8.5" rx="1"/><path d="M3.5 5h3M5 3.5v3"/></g></symbol>
    <symbol id="i-card" viewBox="0 0 12 10"><g fill="none" stroke="currentColor" stroke-width="1"><rect x="1" y="1.5" width="10" height="7" rx="1"/><path d="M1 4.5h10"/></g></symbol>
    <symbol id="i-user" viewBox="0 0 10 10"><path d="M5 1a2 2 0 1 1 0 4 2 2 0 0 1 0-4zM1 9.5c0-2.2 1.8-3.5 4-3.5s4 1.3 4 3.5z" fill="currentColor"/></symbol>
    <symbol id="i-bolt" viewBox="0 0 10 10"><path d="M6 .5L2 6h3l-1 3.5L8 4H5z" fill="currentColor"/></symbol>
    <symbol id="i-toggle" viewBox="0 0 12 10"><g fill="none" stroke="currentColor" stroke-width="1.1"><rect x="1" y="2" width="10" height="6" rx="3"/><circle cx="4" cy="5" r="2" fill="currentColor"/></g></symbol>
  </defs>
</svg>

<div class="app">
  <div class="topbar-user">Dana Holt <svg width="9" height="9"><use href="#i-chev-down"/></svg></div>
  <div class="brand"><span class="brand-dot"></span>Nimbus</div>

  <svg class="nav-icon" style="top:160px"><use href="#i-cal"/></svg>
  <svg class="nav-icon" style="top:230px"><use href="#i-db"/></svg>
  <div class="nav-active"><svg class="nav-icon"><use href="#i-bank"/></svg></div>
  <svg class="nav-icon" style="top:366px"><use href="#i-docs"/></svg>
  <svg class="nav-icon" style="top:430px"><use href="#i-cal"/></svg>
  <svg class="nav-icon" style="top:501px"><use href="#i-db"/></svg>

  <section class="list-panel">
    <div class="sources-head"><h2 class="h-title">Data Sources</h2><span class="pill">+ Add</span></div>
    <div class="search">Search <svg><use href="#i-search"/></svg></div>
    <div class="source is-active" style="top:118px"><div class="source-name">Cloudforge – Sandbox</div><div class="source-type">Cloudforge.io</div></div>
    <div class="source" style="top:185px"><div class="source-name">OpenSQL Test 1 (administrator)</div><div class="source-type">OpenSQL</div></div>
    <div class="source" style="top:252px"><div class="source-name">OpenSQL Test 2 (administrator)</div><div class="source-type">OpenSQL</div></div>
    <div class="source" style="top:319px"><div class="source-name">Sadga</div><div class="source-type">Cloudforge.io</div></div>
    <div class="source" style="top:386px"><div class="source-name">Cloudforge Test 1 (master dev)</div><div class="source-type">OpenSQL</div></div>
    <div class="source" style="top:453px"><div class="source-name">CFDC - Field Entry Test</div><div class="source-type">Cloudforge.io</div></div>
    <div class="source" style="top:523px"><div class="source-name">CFDC 44</div><div class="source-type">Cloudforge.io</div></div>
    <div class="source" style="top:590px"><div class="source-name">CFDC 66</div><div class="source-type">OpenSQL</div></div>
    <div class="list-scroll"></div>
  </section>

  <main class="main">
    <div class="detail-head">
      <h1 class="h-title">Cloudforge – Sandbox</h1>
      <span class="pill"><svg><use href="#i-pen"/></svg>Edit</span>
      <span class="pill"><svg><use href="#i-toggle"/></svg>Clone</span>
      <span class="pill"><svg><use href="#i-x"/></svg>Delete</span>
    </div>
    <span class="pill test-conn"><svg><use href="#i-bolt"/></svg>Test Connection</span>

    <div class="info-card">
      <div class="info-col left">
        <div class="info-row"><span class="info-label">Data Source Name</span><span class="info-value">Cloudforge – Sandbox</span></div>
        <div class="info-row"><span class="info-label">Data Source Type</span><span class="info-value">Application</span></div>
        <div class="info-row"><span class="info-label">Status</span><span class="info-value">Active</span></div>
        <div class="info-row"><span class="info-label">Created By</span><span class="info-value">northfield.test</span></div>
        <div class="info-row"><span class="info-label">Last updated By</span><span class="info-value">northfield.test</span></div>
      </div>
      <div class="info-divider"></div>
      <div class="info-col right">
        <div class="info-row"><span class="info-label">Data Source Name</span><span class="info-value">Cloudforge – Sandbox</span></div>
        <div class="info-row"><span class="info-label">Data Source Type</span><span class="info-value">Application</span></div>
        <div class="info-row"><span class="info-label">Status</span><span class="info-value">Active</span></div>
        <div class="info-row"><span class="info-label">Created By</span><span class="info-value">northfield.test</span></div>
      </div>
    </div>

    <div class="objects-head"><h2 class="h-title">Data Objects</h2><span class="pill">+ Add</span></div>
    <div class="object-tabs">
      <svg class="chev"><use href="#i-chev-up"/></svg>Account<svg class="x"><use href="#i-x"/></svg>
      <span class="fields">Fields <span class="pill">+ Add</span></span>
    </div>

    <div class="table-card">
      <div class="grid">
        <div class="grid-row head">
          <span class="cell c-name">Field Name</span><span class="cell c-type">Data Type</span><span class="cell c-pk">Primary Key</span><span class="cell c-rule">Rule Types</span><span class="cell c-sens">Sensitive Data</span><span class="cell c-act">Actions</span>
        </div>
        <div class="grid-row">
          <span class="cell c-name">Office &amp; Supplies</span><span class="cell c-type">Common. Text</span>
          <span class="cell c-pk"><span class="radio on"><svg><use href="#i-tick"/></svg></span></span>
          <span class="cell c-rule"><span class="rl dark">a</span><svg class="ri"><use href="#i-search"/></svg><svg class="ri dark"><use href="#i-copy"/></svg><svg class="ri"><use href="#i-fork"/></svg><svg class="ri"><use href="#i-ring"/></svg><svg class="ri"><use href="#i-play"/></svg></span>
          <span class="cell c-sens"><svg class="ri" style="width:11px;height:11px"><use href="#i-clip"/></svg><svg class="ri" style="width:12px;height:11px"><use href="#i-card"/></svg><svg class="ri" style="width:11px;height:11px"><use href="#i-user"/></svg></span>
          <span class="cell c-act"><svg class="act"><use href="#i-pen"/></svg><svg class="act"><use href="#i-x"/></svg></span>
        </div>
        <div class="grid-row alt">
          <span class="cell c-name">Salaries &amp; Benefits</span><span class="cell c-type">Address. Address Line 3</span>
          <span class="cell c-pk"><span class="radio"></span></span>
          <span class="cell c-rule"><span class="rl">a</span><svg class="ri"><use href="#i-search"/></svg><svg class="ri dark"><use href="#i-copy"/></svg><svg class="ri"><use href="#i-fork"/></svg><svg class="ri"><use href="#i-ring"/></svg><svg class="ri"><use href="#i-play"/></svg></span>
          <span class="cell c-act"><svg class="act"><use href="#i-pen"/></svg><svg class="act"><use href="#i-x"/></svg></span>
        </div>
        <div class="grid-row">
          <span class="cell c-name">Professional Services</span><span class="cell c-type">Common ID</span>
          <span class="cell c-pk"><span class="radio"></span></span>
          <span class="cell c-rule"><span class="rl violet">a</span><svg class="ri green"><use href="#i-search"/></svg><svg class="ri dark"><use href="#i-copy"/></svg><svg class="ri"><use href="#i-fork"/></svg><svg class="ri"><use href="#i-ring"/></svg><svg class="ri"><use href="#i-play"/></svg></span>
          <span class="cell c-act"><svg class="act"><use href="#i-pen"/></svg><svg class="act"><use href="#i-x"/></svg></span>
        </div>
        <div class="grid-row alt">
          <span class="cell c-name">Human Resources</span><span class="cell c-type">Address. Address Line 2</span>
          <span class="cell c-pk"><span class="radio"></span></span>
          <span class="cell c-rule"><span class="rl">a</span><svg class="ri"><use href="#i-search"/></svg><svg class="ri dark"><use href="#i-copy"/></svg><svg class="ri"><use href="#i-fork"/></svg><svg class="ri"><use href="#i-ring"/></svg><svg class="ri"><use href="#i-play"/></svg></span>
          <span class="cell c-act"><svg class="act"><use href="#i-pen"/></svg><svg class="act"><use href="#i-x"/></svg></span>
        </div>
        <div class="group"><svg class="chev"><use href="#i-chev-down"/></svg>Asset<svg class="x"><use href="#i-x"/></svg></div>
        <div class="group"><svg class="chev"><use href="#i-chev-down"/></svg>Asset Relationship<svg class="x"><use href="#i-x"/></svg></div>
        <div class="group"><svg class="chev"><use href="#i-chev-down"/></svg>Asset Token event<svg class="x"><use href="#i-x"/></svg></div>
        <div class="group"><svg class="chev"><use href="#i-chev-down"/></svg>Case<svg class="x"><use href="#i-x"/></svg></div>
      </div>
      <div class="table-scroll"></div>
    </div>
  </main>
</div>
</body>
</html>
```